Chiropractic Office Needs a Poster for Cryotherapy

We are a chiropractic clinic that caters mostly to athletes. We've recently purchased the first whole body cryotherapy unit in San Antonio, TX (for commercial use - the SA Condors have a unit for their facility). We need a professional, attention grabbing poster created for patient education for our lobby area.
Updates

Poster size 20"X30" (horizontal)

SocialHub link: socialhub.example/mervalebackcare

Industry/Entity Type

Education

Requirements
Must have
• Image of the cryotherapy unit

"Schedule your appointment today"

"Like us on SocialHub for Special Promos" (or something along those lines with FB button)

"www.mervalebackcare.example" & "210-555-0193"

"WHOLE BODY CRYOTHERAPY"

"Just 3 Minutes for Whole Body Recovery"

"How it works....
Inside the cryosauna, which is a tall, cylindrical chamber where the client stands, the body is surrounded by hyper-cooled air at an
average temperature of –220˚F for 2 ½ to 3 minutes. Cold sensors in the skin send a signal to the brain which causes blood to rush
to the core. As blood is circulated through the core, toxins are flushed and blood becomes enriched with oxygen and all the
necessary enzymes and nutrients."

"…Accelerate…
When the session ends, the oxygenated, nutrient and enzyme enriched blood rushes back through the body accelerating the natural recovery process. The release of endorphins, metabolic rate, and production of collagen are accelerated"

"…Recovery!
Recovery time is shortened, energy level is dramatically increased, and the endorphin release aids the body in dealing with pain and inflammation. The increase in metabolic rate allows the body to burn more calories and the production of collagen improves whole body skin elasticity and smoothness."

"BENEFITS INCLUDE:
Pain Management
Injury Therapy
Inflammatory Disorders
Rapid Recovery
Performance Enhancement
Metabolic & Immunity Boost
Anti-Aging
Skin Rejuvenation"
Nice to have
• Logo Attached below - we use the black & blue logo in the horizontal format

```html
<!DOCTYPE html>
<html lang="en">
<head>
<meta charset="utf-8">
<title>Whole Body Cryotherapy – Mervale Back Care</title>
<link href="https://fonts.googleapis.com/css2?family=Arimo:ital,wght@0,400;0,700;1,400&family=Tinos&display=swap" rel="stylesheet">
<style>
  :root {
    --ink: #000000;
    --ice: #7ff3ef;
    --ice-soft: #a9f6f2;
    --benefit: #56d8d2;
    --white: #ffffff;
    --band: rgba(20, 24, 26, 0.55);
    --brand-tab: #f2f2f2;
    --brand-ink: #1aa6c8;
  }
  * { margin: 0; padding: 0; box-sizing: border-box; }
  html, body { width: 1200px; height: 796px; overflow: hidden; background: var(--ink); }
  .poster {
    position: relative; width: 1200px; height: 796px; overflow: hidden;
    background: var(--ink); color: var(--white);
    font-family: "Arimo", Arial, sans-serif;
  }
  .smoke { position: absolute; inset: 0; }
  .band { position: absolute; left: 0; background: var(--band); }
  .title {
    position: absolute; left: 0; width: 1196px; top: 24px; text-align: center;
    font-weight: 700; font-size: 39px; letter-spacing: 0.5px; color: var(--ice);
  }
  .tagline {
    position: absolute; left: 0; width: 1200px; top: 78px; text-align: center;
    font-style: italic; font-size: 26.5px; color: var(--ice-soft);
  }
  .step { position: absolute; left: 38px; }
  .step h2 { font-weight: 400; font-size: 21px; letter-spacing: 1.2px; line-height: 24px; margin-bottom: 1px; }
  .step p { font-size: 17px; line-height: 21px; white-space: nowrap; }
  .step--serif p { font-family: "Tinos", "Times New Roman", serif; font-size: 18px; letter-spacing: 0.7px; line-height: 21px; }
  .unit { position: absolute; left: 905px; top: 24px; width: 272px; height: 448px; }
  .benefits {
    position: absolute; left: 895px; width: 260px; top: 483px; text-align: center;
    list-style: none; font-style: italic; font-size: 18.6px; line-height: 22.8px; color: var(--benefit);
  }
  .contact { position: absolute; left: 0; top: 620px; width: 900px; }
  .contact p { position: absolute; white-space: nowrap; }
  .contact .cta { left: 403px; top: 1px; font-size: 26.5px; color: var(--ice); }
  .contact .phone { left: 504px; top: 45px; font-size: 18.8px; letter-spacing: 0.5px; }
  .contact .social-mark { position: absolute; left: 397px; top: 58px; width: 35px; height: 35px; background: var(--ice); border-radius: 3px; }
  .contact .social { left: 441px; top: 71px; font-size: 20px; color: var(--ice-soft); }
  .contact .social-url { left: 496px; top: 98px; font-size: 20px; color: var(--ice-soft); }
  .contact .web { left: 500px; top: 125px; font-size: 20px; color: var(--ice-soft); }
  .brand-tab {
    position: absolute; left: 815px; top: 706px; width: 400px; height: 100px;
    background: var(--brand-tab); border-top-left-radius: 46px;
  }
  .brand {
    position: absolute; left: 860px; top: 735px; display: flex; align-items: center; gap: 14px;
    font-size: 21px; letter-spacing: 2px; color: var(--brand-ink); white-space: nowrap;
  }
  .brand .mark { width: 44px; height: 30px; background: var(--brand-ink); }
</style>
</head>
<body>
<main class="poster">
  <svg class="smoke" width="1200" height="796" role="img" aria-label="Swirling teal cold-vapour smoke on black background">
    <defs>
      <radialGradient id="mist" cx="50%" cy="50%" r="50%">
        <stop offset="0" stop-color="#2a8f8a" stop-opacity="0.55"/>
        <stop offset="1" stop-color="#2a8f8a" stop-opacity="0"/>
      </radialGradient>
    </defs>
    <ellipse cx="180" cy="80" rx="230" ry="120" fill="url(#mist)"/>
    <ellipse cx="560" cy="250" rx="260" ry="90" fill="url(#mist)" opacity="0.5"/>
    <ellipse cx="120" cy="690" rx="260" ry="150" fill="url(#mist)"/>
    <ellipse cx="600" cy="470" rx="200" ry="80" fill="url(#mist)" opacity="0.4"/>
  </svg>

  <div class="band" style="top:150px;width:900px;height:140px"></div>
  <div class="band" style="top:322px;width:900px;height:100px"></div>
  <div class="band" style="top:455px;width:900px;height:120px"></div>

  <h1 class="title">WHOLE BODY CRYOTHERAPY</h1>
  <p class="tagline">“Just 3 Minutes for Whole Body Recovery”</p>

  <section class="step step--serif" style="top:162px">
    <h2>How it works....</h2>
    <p>Inside the cryosauna, which is a tall, cylindrical chamber where the client stands,<br>
    the body is surrounded by hyper-cooled air at an average temperature of –220˚F for 2 ½ to 3 minutes.<br>
    Cold sensors in the skin send a signal to the brain which causes blood to rush to the core.<br>
    As blood is circulated through the core, toxins are flushed and blood becomes enriched with oxygen<br>
    and all the necessary enzymes and nutrients.</p>
  </section>

  <section class="step" style="top:330px">
    <h2>…Accelerate…</h2>
    <p>When the session ends, the oxygenated, nutrient and enzyme enriched blood<br>
    rushes back through the body accelerating the natural recovery process.<br>
    The release of endorphins, metabolic rate, and production of collagen are accelerated.</p>
  </section>

  <section class="step" style="top:463px">
    <h2>…Recovery!</h2>
    <p>Recovery time is shortened, energy level is dramatically increased,<br>
    and the endorphin release aids the body in dealing with pain and inflammation.<br>
    The increase in metabolic rate allows the body to burn more calories<br>
    and the production of collagen improves whole body skin elasticity and smoothness.</p>
  </section>

  <svg class="unit" viewBox="0 0 272 448" role="img" aria-label="Cylindrical whole body cryotherapy chamber with open door and vapour">
    <defs>
      <linearGradient id="steel" x1="0" x2="1">
        <stop offset="0" stop-color="#5b6673"/>
        <stop offset="0.45" stop-color="#c9ced4"/>
        <stop offset="1" stop-color="#3e4855"/>
      </linearGradient>
    </defs>
    <rect x="0" y="0" width="272" height="448" rx="30" fill="#f4f6f7"/>
    <rect x="14" y="20" width="244" height="418" rx="28" fill="url(#steel)"/>
  </svg>

  <ul class="benefits">
    <li>"BENEFITS INCLUDE:</li>
    <li>Pain Management</li>
    <li>Injury Therapy</li>
    <li>Inflammatory Disorders</li>
    <li>Rapid Recovery</li>
    <li>Performance Enhancement</li>
    <li>Metabolic &amp; Immunity Boost</li>
    <li>Anti-Aging</li>
    <li>Skin Rejuvenation"</li>
  </ul>

  <section class="contact">
    <p class="cta">Schedule your appointment today</p>
    <p class="phone">CALL:&nbsp; 210-555-0193</p>
    <span class="social-mark" aria-hidden="true"></span>
    <p class="social">Like us on SocialHub for Special Promos</p>
    <p class="social-url">socialhub.example/mervalebackcare</p>
    <p class="web">www.mervalebackcare.example</p>
  </section>

  <div class="brand-tab"></div>
  <div class="brand"><span class="mark" aria-hidden="true"></span><span>MERVALE BACK CARE</span></div>
</main>
</body>
</html>
```